I am a Financial Adviser specialising in Aged Care Advice. We provide financial advice and assistance to families with loved ones entering an Aged Care facility.
We need a flyer detailing the Aged Care Packages that we offer. There will be 3 main packages & then other add ons. I need an area where the client can sign off on the package/s that they choose. I have attached a sample to demonstrate the required layout, and a copy of content. I would like the flyer to have an image as per the attached sample, and to be designed in soft pastels, blues, greens.

Financial

```html
<!DOCTYPE html>
<html lang="en">
<head>
<meta charset="utf-8">
<title>Aged Care Services Flyer</title>
<link href="https://fonts.googleapis.com/css2?family=Libre+Baskerville:wght@400;700&family=Didact+Gothic&family=Parisienne&display=swap" rel="stylesheet">
<style>
  :root{
    --bg:#ece9e3;
    --sage:#9fb47a;
    --sage-deep:#6f8a4a;
    --sage-pale:#dfe8cd;
    --olive-text:#4d5f2c;
    --gold:#b8922e;
    --ink:#333;
    --muted:#666;
    --paper:#fff;
  }
  *{box-sizing:border-box;margin:0;padding:0}
  html,body{width:1200px;height:1000px;overflow:hidden}
  body{background:var(--bg);font-family:"Didact Gothic",Arial,sans-serif;color:var(--ink);position:relative}

  .flyer{position:absolute;top:100px;width:500px;height:800px;border-radius:6px;overflow:hidden;box-shadow:0 6px 18px rgba(0,0,0,.18)}
  .flyer--front{left:70px;background:linear-gradient(180deg,var(--sage-pale) 0%,#c9d8ae 55%,var(--sage) 100%)}
  .flyer--back{left:630px;background:linear-gradient(180deg,#c6d5a8,var(--sage));padding:16px}

  /* front */
  .hero-photo{position:absolute;left:0;top:0;width:500px;height:330px;
    background:linear-gradient(180deg,#dfe9d2 0%,#b7cb8d 45%,#9db768 75%,rgba(201,216,174,0) 100%)}
  .brand{position:absolute;left:0;right:0;top:234px;display:flex;justify-content:center;align-items:center;gap:7px;font-family:"Libre Baskerville",Georgia,serif;font-weight:700;font-size:15px;color:var(--olive-text);letter-spacing:.5px}
  .brand__mark{width:9px;height:9px;background:var(--gold)}
  .title{position:absolute;left:0;right:0;top:264px;text-align:center;white-space:nowrap;font-family:"Libre Baskerville",Georgia,serif;font-weight:700;font-size:38px;line-height:46px;color:var(--gold);letter-spacing:.5px;text-shadow:0 1px 0 #fff8dc}

  .package{position:absolute;left:22px;width:456px;height:122px;background:var(--paper);border-radius:12px;box-shadow:0 2px 6px rgba(0,0,0,.18);padding:12px 16px 10px 40px}
  .package--essentials{top:338px}
  .package--advantage{top:474px}
  .package--platinum{top:610px}
  .check{position:absolute;left:14px;top:13px;width:15px;height:15px;border:1.5px solid var(--ink);background:#fff}
  .package__head{font-family:"Libre Baskerville",Georgia,serif;font-size:12.5px;font-weight:700;color:var(--ink);white-space:nowrap}
  .package__head .lead{font-family:"Didact Gothic",Arial,sans-serif;font-weight:400;font-size:10px;color:var(--muted)}
  .package__plus{font-size:11px;font-weight:700;color:var(--gold);margin-top:3px}
  .package__list{list-style:none;font-size:9.5px;line-height:1.4;margin-top:3px;color:var(--ink)}
  .package__list li::before{content:"• ";color:var(--sage-deep)}
  .package__note{font-size:7px;color:var(--muted);margin-top:2px}
  .package__tag{position:absolute;right:18px;bottom:14px;font-family:"Parisienne",cursive;font-size:34px;color:var(--olive-text)}

  /* back */
  .sheet{width:100%;height:100%;background:var(--paper);border-radius:12px;padding:22px 24px}
  .sheet__title{font-family:"Libre Baskerville",Georgia,serif;font-weight:700;font-size:22px;color:var(--olive-text);text-align:center;letter-spacing:1px;margin-bottom:12px}
  .option{position:relative;padding-left:22px;margin-bottom:8px}
  .option .check{left:0;top:1px;width:13px;height:13px}
  .option__name{font-family:"Libre Baskerville",Georgia,serif;font-size:11px;font-weight:700;color:var(--olive-text)}
  .option__desc{font-size:9px;line-height:1.35;color:var(--ink)}
  .declaration{font-size:10.5px;line-height:1.5;margin:14px 4px 0;color:var(--ink)}
  .signatures{display:grid;grid-template-columns:1fr 1fr 1fr;column-gap:18px;row-gap:26px;margin:30px 4px 0}
  .sig{border-top:1px solid #555;padding-top:3px;font-size:9.5px;font-weight:700;color:var(--ink)}
  .sig--date{text-align:center}
  .fine-print{margin:34px 4px 0;font-size:7.5px;line-height:1.4;color:var(--muted)}
  .fine-print strong{display:block;color:var(--ink);font-size:8.5px;margin-bottom:2px}
</style>
</head>
<body>

<section class="flyer flyer--front">
  <div class="hero-photo" role="img" aria-label="Photograph of a smiling three-generation family sitting together on green grass in a sunny park"></div>
  <div class="brand"><span class="brand__mark"></span>Harbour Path Financial</div>
  <h1 class="title">Aged Care Services</h1>

  <article class="package package--essentials">
    <span class="check"></span>
    <p class="package__head">ESSENTIALS Package $770 <span class="lead">........ When you know what you want...</span></p>
    <ul class="package__list">
      <li>Explanation of Aged Care fees and charges</li>
      <li>Preliminary review of assets and income</li>
      <li>Estimated means tested fee calculation</li>
      <li>Estimated cash flow scenario</li>
    </ul>
    <p class="package__note">*Fees shown include GST and apply per family.</p>
    <span class="package__tag">Peace of Mind</span>
  </article>

  <article class="package package--advantage">
    <span class="check"></span>
    <p class="package__head">ADVANTAGE Package $2,970 <span class="lead">...... When you need to know all the options...</span></p>
    <p class="package__plus">ESSENTIALS Package plus</p>
    <ul class="package__list">
      <li>Analysis of strategies to manage Aged Care costs</li>
      <li>Comparison of payment options available</li>
      <li>Statement of Advice (SOA)</li>
    </ul>
    <span class="package__tag">Confidence</span>
  </article>

  <article class="package package--platinum">
    <span class="check"></span>
    <p class="package__head">PLATINUM Package $5,940 <span class="lead">...... When you need someone to take charge...</span></p>
    <p class="package__plus">ADVANTAGE Package plus</p>
    <ul class="package__list">
      <li>Liaise with the Aged Care facility</li>
      <li>Lodge Benefits Office forms</li>
      <li>Post entry review of SOA (if required)</li>
    </ul>
    <span class="package__tag">Convenience</span>
  </article>
</section>

<section class="flyer flyer--back">
  <div class="sheet">
    <h2 class="sheet__title">EXTRA CHOICE OPTIONS</h2>

    <div class="option"><span class="check"></span>
      <p class="option__name">Benefits Office Nominee $1,100</p>
      <p class="option__desc">Correspond with the Benefits Office on behalf of our clients, and undertake all changes and updates to details as directed by the client.</p></div>
    <div class="option"><span class="check"></span>
      <p class="option__name">Post Implementation Statement of Advice $1,650</p>
      <p class="option__desc">Review of our original advice following any change of circumstances including income and asset levels, and provide further advice within 12 months of the initial statement.</p></div>
    <div class="option"><span class="check"></span>
      <p class="option__name">Annual Review $990</p>
      <p class="option__desc">A review of recommendations made in our original advice, taking into account any change in circumstances, including checking current cash flow remains sufficient.</p></div>
    <div class="option"><span class="check"></span>
      <p class="option__name">Post Entry Review $660</p>
      <p class="option__desc">Review facility invoices are accurate and explain the Residential Aged Care Agreement and recommendations implemented.</p></div>
    <div class="option"><span class="check"></span>
      <p class="option__name">Facility Liaison $330</p>
      <p class="option__desc">Negotiate with the Aged Care facility regarding accommodation payments and costs.</p></div>
    <div class="option"><span class="check"></span>
      <p class="option__name">Family Conference $660</p>
      <p class="option__desc">Facilitate a family meeting to explain Aged Care legislation and how it fits with the family circumstances.</p></div>
    <div class="option"><span class="check"></span>
      <p class="option__name">Estate Wrap $660</p>
      <p class="option__desc">Assist beneficiaries with current procedures and paperwork regarding the finalisation of the estate.</p></div>

    <p class="declaration">I/We have chosen the Service Package and Options as ticked above. I/We understand that by choosing the Essentials Package, I/We are receiving factual information only, and not financial advice. I/We agree to pay the amount of ________ within seven days of the date of the invoice received from Harbour Path Financial.</p>

    <div class="signatures">
      <span class="sig">Signature</span><span class="sig">Signature</span><span class="sig">Signature</span>
      <span class="sig">Adviser Signature</span><span class="sig sig--date">Date &nbsp; / &nbsp; /</span><span class="sig sig--date">Date &nbsp; / &nbsp; /</span>
    </div>

    <p class="fine-print"><strong>Important Information</strong>This flyer has been prepared by Harbour Path Advisory Pty Ltd, an Authorised Representative of a licensed advice provider. Information is based on current legislation and rates as at the date of issue, which may be subject to change. It is general in nature and does not take into account your personal objectives, financial situation or needs. You should seek advice before making a financial decision.</p>
  </div>
</section>

</body>
</html>
```